Letterhead for denture company

We need a letterhead designed for our denture company called "Brightmolars" We have attached the logo and business card with the colours on them that we like

Target Market(s)

Everyone aged 45+

Industry/Entity Type

Dental Clinic

Font styles to use
Serif
Sans Serif

Colors
3276b5
f37122

Requirements
Must have
• The colours used in our business card
• Be bold and modern
• Thick fonts
• Logo
Nice to have
• Elements that could tie in nicely with any future signage or website upgrades
Should not have
• Thin font
• Should not be too busy

```html
<!DOCTYPE html>
<html lang="en">
<head>
<meta charset="utf-8">
<title>Brightmolars Letterhead</title>
<link href="https://fonts.googleapis.com/css2?family=Bitter:wght@400;500&family=Open+Sans:wght@400;700&display=swap" rel="stylesheet">
<style>
  :root {
    --brand-blue: #1a6fb8;
    --brand-orange: #e0692f;
    --ink: #222222;
    --paper: #ffffff;
  }
  * { margin: 0; padding: 0; box-sizing: border-box; }
  html, body { width: 959px; height: 1200px; overflow: hidden; background: var(--paper); }
  .letterhead { position: relative; width: 959px; height: 1200px; background: var(--paper); }

  .brand { position: absolute; left: 42px; top: 40px; width: 330px; text-align: center; }
  .brand-square { display: block; width: 68px; height: 66px; margin: 0 auto 8px; background: var(--brand-blue); }
  .brand-name {
    font-family: "Open Sans", sans-serif; font-weight: 700; font-size: 33px;
    letter-spacing: 1px; color: var(--brand-blue); text-transform: uppercase; line-height: 1;
  }

  .address-divider { position: absolute; left: 597px; top: 33px; width: 2px; height: 52px; background: var(--brand-blue); }
  .address { position: absolute; left: 616px; top: 40px; display: flex; gap: 8px; }
  .address svg { margin-top: 4px; flex: none; }
  .address-text { font-family: "Bitter", serif; font-size: 17px; line-height: 22px; color: var(--ink); }

  .footer-bands { position: absolute; left: 0; bottom: 0; }
  .contact-row {
    position: absolute; left: 34px; top: 1151px; display: flex; align-items: center; gap: 22px;
    font-size: 17px; color: var(--ink);
  }
  .contact-item { display: flex; align-items: center; gap: 6px; }
  .contact-item.sans { font-family: "Open Sans", sans-serif; }
  .contact-item.serif { font-family: "Bitter", serif; }
  .website {
    position: absolute; left: 616px; top: 1164px; display: flex; align-items: center; gap: 8px;
    font-family: "Bitter", serif; font-size: 17px; color: var(--paper);
  }
</style>
</head>
<body>
<main class="letterhead">
  <header>
    <div class="brand">
      <span class="brand-square"></span>
      <div class="brand-name">Brightmolars</div>
    </div>

    <div class="address-divider"></div>
    <div class="address">
      <svg width="20" height="18" viewBox="0 0 20 18" aria-hidden="true">
        <path d="M10 1 L19 9 L16.5 9 L16.5 17 L12 17 L12 12 L8 12 L8 17 L3.5 17 L3.5 9 L1 9 Z" fill="var(--brand-blue)"/>
      </svg>
      <div class="address-text">148 Harbour View Road, Kelston South<br>Auckland 0602</div>
    </div>
  </header>

  <footer>
    <svg class="footer-bands" width="959" height="60" viewBox="0 0 959 60" aria-hidden="true">
      <polygon points="0,38 552,38 540,60 0,60" fill="var(--brand-orange)"/>
      <polygon points="606,13 959,13 959,60 548,60" fill="var(--brand-blue)"/>
    </svg>

    <div class="contact-row">
      <div class="contact-item sans">
        <svg width="16" height="16" viewBox="0 0 16 16" aria-hidden="true">
          <circle cx="8" cy="8" r="7" fill="none" stroke="var(--brand-blue)" stroke-width="1.4"/>
          <path d="M9.5 4 Q6 6 6.5 11 L8 11.5 Q7.8 8 10.5 5.5 Z" fill="var(--brand-blue)"/>
        </svg>
        0800 55 7100
      </div>
      <div class="contact-item sans">
        <svg width="11" height="17" viewBox="0 0 11 17" aria-hidden="true">
          <rect x="1" y="1" width="9" height="15" rx="1.5" fill="none" stroke="var(--brand-blue)" stroke-width="1.5"/>
          <rect x="3" y="3.5" width="5" height="4" fill="var(--brand-blue)"/>
          <rect x="3" y="10" width="5" height="3.5" fill="var(--brand-blue)"/>
        </svg>
        09 555 0142
      </div>
      <div class="contact-item serif">
        <svg width="20" height="14" viewBox="0 0 20 14" aria-hidden="true">
          <rect x="0" y="0" width="20" height="14" fill="var(--brand-blue)"/>
          <path d="M0 0 L10 8 L20 0" fill="none" stroke="#ffffff" stroke-width="1.5"/>
        </svg>
        sam@brightmolars.co.nz
      </div>
    </div>

    <div class="website">
      <svg width="16" height="16" viewBox="0 0 16 16" aria-hidden="true">
        <g fill="none" stroke="#ffffff" stroke-width="1.1">
          <circle cx="8" cy="8" r="7"/>
          <ellipse cx="8" cy="8" rx="3" ry="7"/>
          <line x1="1" y1="8" x2="15" y2="8"/>
          <path d="M2.5 4.5 H13.5 M2.5 11.5 H13.5"/>
        </g>
      </svg>
      www.brightmolars.co.nz
    </div>
  </footer>
</main>
</body>
</html>
```